flyer design for landscape group. i have enclosed my business card with logo

we are a local domestic and commercial landscaping group based in wokingham berkshire .we offer competitive landscaping solutions with a broad knowledge helping us solve problems in many fields such as new lawns, lawn care,tree care ,tree removal,hard and soft landscaping, decking, fencing ,garden or land clearance or just helping you with general maintanence. Being fully insured and certified for the job ,our excellent attention to detail has seen us recognised by local authorities and work for them on maintenance programmes performing in a safe and efficient manner

Target Market(s)

high end gardens commercial property

Industry/Entity Type

Landscaping

Requirements
Must have
• my logo . and some minimal sleek black and white design with small injections of colour
Should not have
• please do not include my full name or address only email and telephone

```html
<!DOCTYPE html>
<html lang="en">
<head>
<meta charset="utf-8">
<title>Canopy Berkshire – Landscaping Services</title>
<link rel="stylesheet" href="https://fonts.googleapis.com/css2?family=Roboto:wght@300;400&display=swap">
<style>
  :root {
    --page: #ffffff;
    --frame: #e2e2e2;
    --forest: #143f12;
    --stone: #e2dedb;
    --bark: #3a2b24;
    --amber: #f0861c;
    --text-light: #f2f2ee;
  }
  * { margin: 0; padding: 0; box-sizing: border-box; }
  html, body {
    width: 1200px;
    height: 901px;
    overflow: hidden;
    background: var(--page);
  }
  .canvas {
    position: relative;
    width: 1200px;
    height: 901px;
    border: 2px solid var(--frame);
    background: var(--page);
    font-family: "Roboto", Arial, sans-serif;
  }
  .panel { position: absolute; }
  .photo-leaves {
    left: 325px; top: 53px; width: 324px; height: 464px;
    background:
      radial-gradient(ellipse at 30% 30%, #c8cac8 0%, rgba(200,202,200,0) 55%),
      radial-gradient(ellipse at 70% 80%, #b5b7b5 0%, rgba(181,183,181,0) 50%),
      linear-gradient(135deg, #9a9c9a 0%, #4a4c4b 45%, #8e908e 70%, #2e302f 100%);
  }
  .services {
    left: 659px; top: 53px; width: 217px; height: 464px;
    background: var(--forest);
    color: var(--text-light);
  }
  .service-list {
    list-style: none;
    position: absolute;
    top: 105px; left: 0; width: 100%;
    text-align: center;
    font-size: 14px;
    font-weight: 300;
    letter-spacing: 0.4px;
    line-height: 33.6px;
  }
  .brand {
    left: 325px; top: 528px; width: 323px; height: 322px;
    background: var(--stone);
    color: var(--bark);
    text-align: center;
  }
  .brand-mark {
    position: absolute;
    left: 150px; top: 92px;
    width: 24px; height: 24px;
    background: var(--amber);
  }
  .brand-name {
    position: absolute;
    left: 0; width: 100%;
    top: 190px;
    font-weight: 300;
    font-size: 40px;
    letter-spacing: 2px;
    line-height: 1;
  }
  .brand-region {
    display: block;
    margin-top: 12px;
    font-size: 17px;
    letter-spacing: 3px;
  }
  .photo-fern {
    left: 659px; top: 528px; width: 217px; height: 322px;
    background:
      radial-gradient(ellipse at 85% 55%, #9b9d9c 0%, rgba(155,157,156,0) 45%),
      radial-gradient(ellipse at 20% 20%, #5a5c5b 0%, rgba(90,92,91,0) 50%),
      linear-gradient(160deg, #2a2b2b 0%, #1b1c1c 55%, #3a3b3b 100%);
  }
</style>
</head>
<body>
  <main class="canvas">
    <div class="panel photo-leaves" role="img" aria-label="Black and white photograph of maple leaves and fern fronds"></div>

    <section class="panel services">
      <ul class="service-list">
        <li>New Lawns</li>
        <li>Lawn Care</li>
        <li>Tree Care</li>
        <li>Tree Removal</li>
        <li>Hard &amp; Soft Landscaping</li>
        <li>Desking &amp; Fencing</li>
        <li>Garden or Land Clearance</li>
        <li>General Maintenance</li>
      </ul>
    </section>

    <section class="panel brand">
      <span class="brand-mark"></span>
      <p class="brand-name">CANOPY<span class="brand-region">BERKSHIRE</span></p>
    </section>

    <div class="panel photo-fern" role="img" aria-label="Dark black and white close-up photograph of a fern frond"></div>
  </main>
</body>
</html>
```